We need a postcard design for a new company based in the Midwest named Dorsey Consulting Service. We serve the food manufacturing industry. We provide food manufacturers with services to assist them in acquiring certification to meet the Allied Kitchen Trust Program (AKTP). I audit on several auditing platforms: TLV, MDN, KVR 48100, PLNX 37500, HACCP. We also train on food safety pre-requisite programs (Food Defense, GMP's, Emergency Preparedness, Sanitation, Glass & Brittle Plastic, Allergen Control, Purchased Material, Harlan Provisions Reform Act, etc.) We would like designs that list what we offer and prefer colors in Green. The final design should communicate "Working in Partnership to achieve Excellence" "Common Sense Approach to Food Safety"

Target Market(s)

Food Manufacturer Companies - Quality Assurance Managers, Food Safety Managers, Food Safety Coordinators.

Industry/Entity Type

Auditing

Requirements
Must have
• The postcard must have Dorsey Consulting Service, address, phone number, and Wade Dorsey as Consultant.
Should not have
• I want to avoid using comic type of wording or logos. It has to be professional in nature.

```html
<!DOCTYPE html>
<html lang="en">
<head>
<meta charset="utf-8">
<title>Dorsey Consulting Services – Postcard</title>
<link rel="stylesheet" href="https://fonts.googleapis.com/css2?family=Questrial&family=Source+Sans+3:wght@400;600&display=swap">
<style>
  :root {
    --green-dark: #0e8a3e;
    --green-mid: #1a9a45;
    --green-box: #1f8a40;
    --lime: #8dc63f;
    --lime-soft: #b5da7e;
    --lime-text: #5cb531;
    --body-text: #555555;
    --contact-text: #4a4a4a;
    --white: #ffffff;
  }
  html, body { margin: 0; padding: 0; overflow: hidden; }
  body { width: 930px; height: 1200px; background: var(--white); }
  .postcard { position: relative; width: 930px; height: 1200px; overflow: hidden; background: var(--white); }
  .corner { position: absolute; }
  .corner-top { left: 0; top: 0; }
  .corner-bottom { right: 0; bottom: 0; }

  .brand-title {
    position: absolute; left: 409px; top: 52px; margin: 0;
    font-family: "Source Sans 3", sans-serif; font-weight: 400;
    font-size: 35px; letter-spacing: 0.1px; color: var(--green-dark); white-space: nowrap;
  }
  .brand-title strong { font-weight: 600; }
  .produce-icons { position: absolute; left: 408px; top: 105px; }

  .hero-photo {
    position: absolute; left: 410px; top: 164px; width: 440px; height: 266px;
    background: radial-gradient(circle at 70% 40%, #f5c84a 0%, #e85a3a 35%, #b8253a 70%, #6a1a2a 100%);
  }
  .hero-wedge { position: absolute; left: 410px; top: 164px; }
  .hero-tagline {
    position: absolute; left: 454px; top: 204px; margin: 0;
    font-family: "Source Sans 3", sans-serif; font-size: 24px; line-height: 27px; color: var(--white);
  }

  .about { position: absolute; left: 76px; top: 160px; width: 290px; }
  .about-heading {
    margin: 0 0 22px; font-family: "Questrial", sans-serif; font-weight: 400;
    font-size: 21px; color: var(--green-dark);
  }
  .about p, .training p {
    margin: 0 0 22px; font-family: "Questrial", sans-serif;
    font-size: 16.5px; line-height: 22.5px; color: var(--body-text);
  }

  .emblem-area {
    position: absolute; left: 76px; top: 504px; width: 220px; height: 220px;
    background: linear-gradient(135deg, var(--lime-soft) 0%, var(--lime) 100%);
  }
  .partnership { position: absolute; left: 348px; top: 496px; }
  .headline {
    margin: 0; font-family: "Source Sans 3", sans-serif; font-weight: 400;
    font-size: 42px; line-height: 44px; color: var(--green-dark); letter-spacing: -0.4px;
  }
  .subline {
    margin: 0; font-family: "Source Sans 3", sans-serif; font-weight: 400;
    font-size: 27px; line-height: 32px; color: var(--lime-text);
  }
  .training { position: absolute; left: 348px; top: 614px; width: 510px; }

  .brand-panel {
    position: absolute; left: 76px; top: 793px; width: 378px; height: 156px;
    background: linear-gradient(120deg, var(--green-mid) 0%, var(--green-mid) 25%, var(--green-box) 25%, var(--green-box) 100%);
  }
  .brand-panel-name {
    position: absolute; left: 48px; top: 59px; margin: 0;
    font-family: "Source Sans 3", sans-serif; font-weight: 400; font-size: 26px; color: var(--white);
  }
  .brand-panel-arrow { position: absolute; left: 272px; top: 51px; }

  .approach { position: absolute; left: 496px; top: 786px; }
  .approach .headline { font-size: 43px; line-height: 42px; }
  .approach .subline { margin-top: 4px; }

  .contact { position: absolute; left: 76px; top: 1014px; }
  .contact-heading {
    margin: 0 0 26px; font-family: "Source Sans 3", sans-serif; font-weight: 400;
    font-size: 19px; color: var(--green-dark);
  }
  .contact-list { margin: 0; padding: 0; list-style: none; }
  .contact-list li {
    font-family: "Source Sans 3", sans-serif; font-size: 16px; line-height: 27.5px; color: var(--contact-text);
  }
  .contact-list b { font-weight: 600; }
  .contact-gap { display: inline-block; width: 14px; }
</style>
</head>
<body>
<main class="postcard">
  <svg class="corner corner-top" width="180" height="180" viewBox="0 0 180 180" aria-hidden="true">
    <defs><linearGradient id="cornerFadeTop" x1="0" y1="0" x2="1" y2="1"><stop offset="0" stop-color="#0e8a3e"/><stop offset="1" stop-color="#22a84a"/></linearGradient></defs>
    <polygon points="0,0 180,0 0,180" fill="url(#cornerFadeTop)"/>
  </svg>

  <h1 class="brand-title"><strong>DORSEY</strong> CONSULTING SERVICES</h1>

  <svg class="produce-icons" width="444" height="44" viewBox="0 0 444 44" role="img" aria-label="Row of seven round produce icons: cherries, pineapple, apple, egg, melon, grapes, strawberry">
    <g fill="#0e8a3e">
      <circle cx="22" cy="22" r="21.5"/><circle cx="86" cy="22" r="21.5"/><circle cx="151" cy="22" r="21.5"/>
      <circle cx="216" cy="22" r="21.5"/><circle cx="281" cy="22" r="21.5"/><circle cx="346" cy="22" r="21.5"/>
      <circle cx="420" cy="22" r="21.5"/>
    </g>
  </svg>

  <div class="hero-photo" role="img" aria-label="Photo of a pile of red and yellow nectarines"></div>
  <svg class="hero-wedge" width="268" height="266" viewBox="0 0 268 266" aria-hidden="true">
    <polygon points="0,0 268,0 0,266" fill="#8dc63f"/>
  </svg>
  <p class="hero-tagline">Think<br>quickly.</p>

  <section class="about">
    <h2 class="about-heading">About us</h2>
    <p>We serve the food manufacturing industry. We provide food manufacturers with services to assist them in acquiring certification to meet the Allied Kitchen Trust Program (AKTP).</p>
    <p>I audit on several auditing platforms: TLV, MDN, KVR 48100, PLNX 37500, HACCP.</p>
  </section>

  <div class="emblem-area" role="img" aria-label="Decorative lime green triangle emblem"></div>

  <section class="partnership">
    <h2 class="headline">WORKING IN PARTNERSHIP</h2>
    <p class="subline">TO ACHIEVE EXCELLENCE</p>
  </section>

  <section class="training">
    <p>We also train on food safety pre-requisite programs:</p>
    <p>Food Defense, GMP's, Emergency Preparedness, Sanitation, Glass &amp; Brittle Plastic, Allergen Control, Purchased Material, Harlan Provisions Reform Act, etc.</p>
  </section>

  <div class="brand-panel">
    <p class="brand-panel-name">DorseyConsulting</p>
    <svg class="brand-panel-arrow" width="56" height="56" viewBox="0 0 56 56" aria-hidden="true">
      <circle cx="28" cy="28" r="24" fill="none" stroke="#ffffff" stroke-width="3.5"/>
      <path d="M16 28 H38 M29 19 L38 28 L29 37" fill="none" stroke="#ffffff" stroke-width="3.5" stroke-linecap="round" stroke-linejoin="round"/>
    </svg>
  </div>

  <section class="approach">
    <h2 class="headline">COMMON SENSE<br>APPROACH</h2>
    <p class="subline">TO FOOD SAFETY</p>
  </section>

  <section class="contact">
    <h2 class="contact-heading">Contact Wade Dorsey</h2>
    <ul class="contact-list">
      <li><b>A:</b> 418 Linden Court, Fairview, Iowa,&nbsp; 52290</li>
      <li><b>P:</b> 555-210-4387<span class="contact-gap"></span>555-684-9021</li>
      <li><b>M:</b> contact@dorseyconsult.net</li>
    </ul>
  </section>

  <svg class="corner corner-bottom" width="186" height="186" viewBox="0 0 186 186" aria-hidden="true">
    <defs><linearGradient id="cornerFadeBottom" x1="1" y1="0" x2="0" y2="1"><stop offset="0" stop-color="#22a84a"/><stop offset="1" stop-color="#0e8a3e"/></linearGradient></defs>
    <polygon points="186,0 186,186 0,186" fill="url(#cornerFadeBottom)"/>
  </svg>
</main>
</body>
</html>
```